Stationary Design for Quince consultant and support company

We need new stationary designed for a London based support company that provide on-site and remote support services for Quince products. Our clients are both consumers and businesses.

We would like a letterhead, compliment slip, business card and possibly an e-mail signature designed.

Business card designs can be either 1 side or 2, depending on designs we receive we may choose a preference for 1 or 2 sides later on in the design stage.

Designs needs to be at least 300dpi and should be done using CMYK colours.

We want the design to be bold, easy to read, clean and professional.

We have attached our company logo in 2 colour variations (if you need any other source files then please ask).

Our logo colours are as follows:

Blue (85, 50, 0, 0) and Green (50, 0, 100, 0)

We use two different suppliers for out stationary so here are the size dimensions for both. Unfortunately they are ever so slightly different size wise so hopefully we can get something that accommodates both, we can provide dimensions if required for final versions.

Some fonts that have been used before with our company are Probert (for tagline on our company logo) and previously had Nauman used, however we are very much open to seeing what the designers come up with and the fonts mentioned are not a requirement.
Updates

Company details for designs (however the template should be editable for multiple staff) Vorn-Q Ltd. Registered Office: 62-74 Marrow Lane London N7 3QT 020 7195 8843 www.vorn-q.co info@vorn-q.co Company is Registered in England and Wales Company No. 06412853 Directors details (if you want to make the template using his details), rest of the details are as above Dan Myles Director dan@vorn-q.co

Hi all, Thank you for your submissions so far. Could we please ask that you don't use the logo with the tagline from our website for the stationary designs and only the logos provided in the design brief. For the business cards we are looking at normal rectangular business cards to be used and we can provide a template guide for size if needed, please just ask. Regards Vorn-Q Team

Target Market(s)

Our target market are consumers (of all ages) and small/medium businesses.

Industry/Entity Type

Business

Font styles to use
Serif
Sans Serif

Requirements
Must have
• At least business card, letterhead and compliment slip submitted (we need all 3 designed this time round)
Should not have
• Business cards should not have the writing "registered office" (letterheads and compliment slips can along the bottom edge)

```html
<!DOCTYPE html>
<html lang="en">
<head>
<meta charset="utf-8">
<title>Vorn-Q Letterhead</title>
<link href="https://fonts.googleapis.com/css2?family=Exo+2:ital,wght@0,400;0,700;1,400&display=swap" rel="stylesheet">
<style>
  :root {
    --brand-blue: #1f6cb5;
    --brand-green: #78b43c;
    --ink: #2b2b2b;
    --ink-soft: #4a4a4a;
    --paper: #f7f7f6;
    --backdrop: #e8edf2;
  }
  html, body {
    margin: 0;
    width: 1200px;
    height: 1000px;
    overflow: hidden;
    background: var(--backdrop);
    font-family: "Exo 2", Arial, sans-serif;
  }
  .letterhead {
    position: absolute;
    left: 270px;
    top: 33px;
    width: 660px;
    height: 934px;
    background: var(--paper);
    box-shadow: 0 2px 8px rgba(0,0,0,0.12);
    color: var(--ink);
  }
  .corner-bands {
    position: absolute;
    left: 0;
    top: 0;
  }
  .brand {
    position: absolute;
    left: 111px;
    top: 70px;
    width: 120px;
    text-align: right;
  }
  .brand-name {
    font-weight: 700;
    font-size: 29px;
    line-height: 1;
    color: var(--ink);
    letter-spacing: 1px;
  }
  .brand-details {
    margin-top: 6px;
    font-size: 6.5px;
    line-height: 9px;
    color: var(--ink-soft);
  }
  .brand-details strong {
    font-weight: 700;
    color: var(--ink);
  }
  .letter-body {
    position: absolute;
    left: 141px;
    top: 250px;
    width: 380px;
    font-size: 9.3px;
    line-height: 13.7px;
    color: var(--ink-soft);
  }
  .salutation {
    font-style: italic;
    font-size: 12px;
    color: var(--ink);
    margin: 0 0 30px;
  }
  .letter-body p.paragraph {
    margin: 0 0 26px;
    text-align: justify;
  }
  .sign-off {
    position: absolute;
    left: 141px;
    top: 712px;
    width: 380px;
    text-align: right;
    font-style: italic;
    font-size: 12px;
    color: var(--ink);
  }
  .signature {
    position: absolute;
    left: 323px;
    top: 758px;
    width: 183px;
    height: 42px;
    background: linear-gradient(90deg, rgba(40,40,40,0.08), rgba(40,40,40,0.14), rgba(40,40,40,0.08));
    border-radius: 4px;
  }
</style>
</head>
<body>
  <main class="letterhead">
    <svg class="corner-bands" width="80" height="190" viewBox="0 0 80 190" aria-hidden="true">
      <rect x="0" y="0" width="44" height="184" fill="var(--brand-blue)"/>
      <rect x="54" y="0" width="14" height="184" fill="var(--brand-green)"/>
    </svg>

    <header class="brand">
      <div class="brand-name">Vorn-Q</div>
      <div class="brand-details">
        <strong>Vorn-Q Ltd. Registered</strong><br>
        62-74 Marrow Lane<br>
        London N7 3QT<br>
        020 7195 8843<br>
        www.vorn-q.co<br>
        info@vorn-q.co
      </div>
    </header>

    <section class="letter-body">
      <p class="salutation">Dear Client,</p>
      <p class="paragraph">Lorem ipsum dolor sit amet, consectetur adipiscing elit. Nulla sodales nisi vitae Lorem ipsum dolor sit amet, consectetur adipiscing elit. Suspendisse feugiat eros nisl, a facilisis risus eleifend sed. Aliquam mauris enim, fermentum eu lacinia sit amet, laoreet eu leo. Nullam eleifend nulla in libero tristique, ac vulputate odio tincidunt. Etiam non condimentum tortor. Integer suscipit neque nec odio porttitor cursus. Phasellus a sapien blandit, suscipit justo id, condimentum ante. Morbi tristique justo risus, id mattis dui molestie ut. Nullam volutpat ut quam commodo faucibus. Pellentesque urna est, interdum in elit quis, pharetra elementum orci. Nam pharetra velit molestie justo placerat scelerisque.</p>
      <p class="paragraph">Sed est tellus, rutrum in nisl a, consequat sollicitudin elit. Aliquam vitae vestibulum felis. Morbi iaculis nunc volutpat diam ullamcorper vestibulum. Nulla facilisi. Aenean accumsan gravida orci, vitae consectetur justo aliquet et. Curabitur vehicula tempus dolor, a gravida metus vestibulum sit amet. Integer non erat elementum, malesuada metus vel, fermentum lectus. Etiam sit amet nisl ac augue semper ultrices.</p>
      <p class="paragraph">Nulla tincidunt molestie libero vel pretium. Donec condimentum nulla sit amet risus semper imperdiet. Duis congue eros nec diam blandit, et pellentesque sapien auctor. Curabitur iaculis enim lectus, in imperdiet mauris mattis eget. Etiam ac ornare metus. Mauris risus leo, egestas at dolor a, ultrices adipiscing est. Nunc faucibus scelerisque mollis. Pellentesque aliquet mauris tellus, id dignissim risus viverra et. Mauris venenatis lobortis eros. Nam id diam in ligula malesuada feugiat. Cras turpis felis, aliquet id mauris elementum, feugiat ultricies nisl.</p>
    </section>

    <p class="sign-off">Best regards.</p>
    <div class="signature" role="img" aria-label="Handwritten signature of the sender"></div>
  </main>
</body>
</html>
```